All Natural Mosquito Repellent

My company, BrightFern Company has created an all natural mosquito repellent. I already have other all natural products that I have developed and created labels for. I will include a copy of that label so you have something to work from. I will need two labels. One for the front of the bottle and one for the back. The back label will need space for a UPC. The labels need to be 63mm (H) x 39mm (W)

Target Market(s)

Consumers, Organic, People who like natural products

Font styles to use
Other font styles liked:
• A combination of both Serif and Sans Serif

Requirements
Must have
• Use the words Organic, All Natural, Travel size, made in the USA label
Nice to have
• tag line: Don't beat them off. Spray them away.

```html
<!DOCTYPE html>
<html lang="en">
<head>
<meta charset="utf-8">
<title>BrightFern Co. – Mosquito Repellent Label Options</title>
<link rel="stylesheet" href="https://fonts.googleapis.com/css2?family=Bangers&family=Barlow:wght@500&family=Roboto+Slab:wght@700&family=Caveat:wght@500&display=swap">
<style>
  :root {
    --bg: #ffffff;
    --heading: #8a8a8e;
    --ink: #2a2a2a;
    --white: #ffffff;
    --forest: #1e2a1e;
    --orange: #d9781f;
    --leaf: #6fb43f;
    --yellow: #e6dd22;
    --lime: #d5cf2c;
    --red: #d42a2a;
    --badge: #2c3a2a;
  }
  * { margin: 0; padding: 0; box-sizing: border-box; }
  html, body { width: 1200px; height: 1053px; overflow: hidden; background: var(--bg); }
  .sheet { position: relative; width: 1200px; height: 1053px; }
  .option-title {
    position: absolute; top: 50px; width: 270px; text-align: center;
    font-family: "Barlow", sans-serif; font-weight: 500; font-size: 58px;
    color: var(--heading); letter-spacing: 1px;
  }
  .label {
    position: absolute; top: 360px; width: 270px; height: 344px;
    background: var(--white); overflow: hidden;
    box-shadow: 0 2px 10px rgba(0,0,0,.12);
  }
  .label-header { position: absolute; inset: 0 0 auto 0; height: 88px; }
  .brand-dot {
    position: absolute; left: 22px; top: 30px; width: 30px; height: 30px;
    border-radius: 50%; background: var(--orange);
  }
  .brand-name {
    position: absolute; left: 60px; top: 31px;
    font-family: "Roboto Slab", serif; font-weight: 700; font-size: 19px; color: var(--ink);
  }
  .brand-tagline {
    position: absolute; left: 62px; top: 56px;
    font-family: "Caveat", cursive; font-size: 12px; color: #555;
  }
  .label-panel {
    position: absolute; left: 0; right: 0; top: 84px; bottom: 0;
    clip-path: polygon(0 8px, 100% 0, 100% 100%, 0 100%);
  }
  .panel-stripe { position: absolute; left: 0; right: 0; top: 84px; height: 6px;
    background: var(--orange); clip-path: polygon(0 8px, 100% 0, 100% 4px, 0 12px); }
  .label-bottom { position: absolute; left: 0; right: 0; bottom: 0; height: 90px; }
  .txt { position: absolute; left: 0; right: 0; text-align: center; font-family: "Bangers", cursive; }
  .all-natural { top: 104px; font-size: 22px; letter-spacing: 1px; color: var(--white); }
  .mosquito { top: 124px; font-size: 66px; letter-spacing: 1px; line-height: 1; }
  .repellent { top: 192px; font-size: 34px; letter-spacing: 1px; line-height: 1; }
  .travel {
    position: absolute; left: 12px; top: 200px; width: 32px; height: 32px; border-radius: 50%;
    border: 2px solid var(--orange); background: var(--forest);
    font-family: "Caveat", cursive; font-size: 9px; color: var(--white);
    display: flex; align-items: center; justify-content: center; text-align: center; line-height: 1;
  }
  .made-usa { position: absolute; left: 10px; top: 272px; display: flex; align-items: center; gap: 4px; }
  .flag-mark { width: 22px; height: 22px; border-radius: 50%; background: #e8e8e8; }
  .made-usa span { font-family: "Bangers", cursive; color: var(--white); font-size: 11px; line-height: 1; }
  .made-usa b { display: block; font-weight: 400; font-size: 20px; }
  .net { top: 280px; font-size: 13px; line-height: 1; }
  .net b { display: block; font-weight: 400; font-size: 24px; }
  .organic {
    position: absolute; right: 8px; top: 248px; width: 66px; height: 66px; border-radius: 50%;
    background: var(--badge); border: 3px solid var(--white);
    display: flex; align-items: center; justify-content: center;
    font-family: "Caveat", cursive; font-size: 20px; color: var(--white); transform: rotate(-14deg);
  }
  .organic-leaves {
    position: absolute; right: 2px; top: 232px; width: 44px; height: 26px;
    border-radius: 50% 0; background: var(--leaf);
  }

  .opt-1 .label-panel { background: var(--forest); }
  .opt-1 .label-bottom { background: var(--orange); }
  .opt-1 .mosquito { color: var(--orange); }
  .opt-1 .repellent { color: var(--leaf); }
  .opt-1 .net { color: var(--forest); }
  .opt-1 .made-usa span { color: var(--forest); }

  .opt-2 .label-panel { background: var(--forest); }
  .opt-2 .all-natural { color: var(--orange); }
  .opt-2 .mosquito { color: var(--yellow); }
  .opt-2 .repellent { color: var(--orange); }
  .opt-2 .net { color: var(--yellow); }

  .opt-3 .label-panel { background: var(--red); }
  .opt-3 .panel-stripe { background: var(--forest); }
  .opt-3 .mosquito { color: var(--lime); }
  .opt-3 .repellent { color: var(--white); }
  .opt-3 .net { color: var(--yellow); }
  .opt-3 .travel { border-color: var(--white); }
</style>
</head>
<body>
<main class="sheet">
  <h2 class="option-title" style="left:124px">Option-01</h2>
  <h2 class="option-title" style="left:464px">Option-02</h2>
  <h2 class="option-title" style="left:804px">Option-03</h2>

  <section class="label opt-1" style="left:124px">
    <div class="label-header"><span class="brand-dot"></span><span class="brand-name">BrightFern Co.</span><span class="brand-tagline">crafted by hand, with love • in the U.S.A.</span></div>
    <div class="label-panel"></div><div class="panel-stripe"></div>
    <div class="label-bottom"></div>
    <div class="txt all-natural">All Natural</div>
    <div class="txt mosquito">Mosquito</div>
    <div class="txt repellent">Repellent</div>
    <div class="travel">Travel<br>size</div>
    <div class="made-usa"><span class="flag-mark" role="img" aria-label="Round flag emblem"></span><span>Made in<b>USA</b></span></div>
    <div class="txt net">Net Weight<b>125 ML</b></div>
    <div class="organic-leaves" role="img" aria-label="Green leaf illustration"></div>
    <div class="organic">Organic</div>
  </section>

  <section class="label opt-2" style="left:464px">
    <div class="label-header"><span class="brand-dot"></span><span class="brand-name">BrightFern Co.</span><span class="brand-tagline">crafted by hand, with love • in the U.S.A.</span></div>
    <div class="label-panel"></div><div class="panel-stripe"></div>
    <div class="txt all-natural">All Natural</div>
    <div class="txt mosquito">Mosquito</div>
    <div class="txt repellent">Repellent</div>
    <div class="travel">Travel<br>size</div>
    <div class="made-usa"><span class="flag-mark" role="img" aria-label="Round flag emblem"></span><span>Made in<b>USA</b></span></div>
    <div class="txt net">Net Weight<b>125 ML</b></div>
    <div class="organic-leaves" role="img" aria-label="Green leaf illustration"></div>
    <div class="organic">Organic</div>
  </section>

  <section class="label opt-3" style="left:804px">
    <div class="label-header"><span class="brand-dot"></span><span class="brand-name">BrightFern Co.</span><span class="brand-tagline">crafted by hand, with love • in the U.S.A.</span></div>
    <div class="label-panel"></div><div class="panel-stripe"></div>
    <div class="txt all-natural">All Natural</div>
    <div class="txt mosquito">Mosquito</div>
    <div class="txt repellent">Repellent</div>
    <div class="travel">Travel<br>size</div>
    <div class="made-usa"><span class="flag-mark" role="img" aria-label="Round flag emblem"></span><span>Made in<b>USA</b></span></div>
    <div class="txt net">Net Weight<b>125 ML</b></div>
    <div class="organic-leaves" role="img" aria-label="Green leaf illustration"></div>
    <div class="organic">Organic</div>
  </section>
</main>
</body>
</html>
```